New Web Site Design - Ironwood Signal Solutions

We are looking for a completely new web site design. Ironwood Signal Solutions is a full service company providing PBX and IP/Cloud Based phone systems. We also sell and install video camera surveillance systems and provide low voltage cabling services (CAT5 and CAT3). We are looking for something professional looking. We want to be able to showcase our vendor partners as well as be able to show photos of some of the work we have done. We will also want to be able to post PDF brochures as well as make changes to the website ourselves.

Target Market(s)

Commercial

Industry/Entity Type

Communication

Coding

Coded - Design and coding required

Number of Pages Required

5+ page

Font styles to use
Sans Serif

Colors
0455a3

Requirements
Must have
• Ability to upload PDF brochures
• Professional look and feel
• Ability to upload and easily insert job photos
• Thinking it should have at least 6 pages: Main page, phone systems and services page, carrier services page, video surveillance systems and service page, low voltage cabling services page, contact us page

```html
<!DOCTYPE html>
<html lang="en">
<head>
<meta charset="utf-8">
<title>Ironwood Signal Solutions</title>
<link href="https://fonts.googleapis.com/css2?family=Questrial&family=Open+Sans:wght@400;600;700&display=swap" rel="stylesheet">
<style>
  :root {
    --navy: #0b3a73;
    --navy-dark: #082e5e;
    --brand: #0455a3;
    --ink: #555b63;
    --ink-dark: #222;
    --line: #c9ccd0;
    --page: #ffffff;
    --topbar: #e3e4e6;
    --footer-top: #d9dadc;
    --footer-bottom: #f1f1f2;
  }
  * { box-sizing: border-box; margin: 0; padding: 0; }
  html, body { width: 950px; height: 1200px; overflow: hidden; background: var(--page); }
  body { font-family: "Open Sans", sans-serif; color: var(--ink); }
  .canvas { position: relative; width: 950px; height: 1200px; overflow: hidden; background: var(--page); }
  .abs { position: absolute; }

  .topbar { left: 0; top: 0; width: 950px; height: 6px; background: var(--topbar); }

  .brand { left: 59px; top: 38px; font-family: "Questrial", sans-serif; font-size: 22px; font-weight: 400; color: var(--navy); line-height: 1; }

  .call { left: 715px; top: 28px; font-family: "Questrial", sans-serif; color: var(--ink-dark); }
  .call-label { font-size: 17px; }
  .call-number { font-size: 26px; color: var(--navy); margin-top: 2px; letter-spacing: 0.3px; }

  .nav { left: 0; top: 101px; width: 950px; height: 36px; background: linear-gradient(var(--brand), var(--navy-dark)); }
  .nav a { position: absolute; top: 9px; font-family: "Questrial", sans-serif; font-size: 14.5px; color: #fff; text-decoration: none; letter-spacing: 0.3px; }

  .hero { left: 0; top: 137px; width: 950px; height: 343px; }
  .hero-photo { position: absolute; inset: 0; background: linear-gradient(100deg, #b86a45 0%, #a5583a 40%, #8e4a30 70%, #b9704c 100%); }
  .hero-title { left: 59px; top: 55px; font-family: "Questrial", sans-serif; font-weight: 400; color: var(--navy); }
  .hero-title .big { font-size: 42px; line-height: 1; }
  .hero-title .small { font-size: 28px; line-height: 1.2; margin-top: 4px; }
  .hero-text { left: 59px; top: 146px; width: 370px; font-size: 17px; line-height: 22px; color: #fff; letter-spacing: 0.2px; }
  .dots { left: 59px; top: 300px; display: flex; gap: 7px; }
  .dots span { width: 9px; height: 9px; border-radius: 50%; background: #fff; }
  .dots span.on { background: var(--navy); }

  .card { top: 594px; width: 262px; height: 219px; border: 1px solid var(--line); background: #fff; text-align: center; }
  .card-shadow { top: 812px; width: 262px; height: 18px; background: radial-gradient(ellipse at top, rgba(0,0,0,0.16), rgba(0,0,0,0) 70%); }
  .card-photo { top: 521px; width: 162px; height: 162px; border-radius: 50%; }
  .card-title { position: absolute; left: 0; right: 0; top: 107px; font-family: "Questrial", sans-serif; font-weight: 700; font-size: 15.5px; color: var(--navy); letter-spacing: 0.4px; }
  .card-text { position: absolute; left: 20px; right: 20px; top: 130px; font-size: 11.4px; line-height: 17.6px; }

  .divider { left: 59px; top: 855px; width: 833px; height: 1px; background: var(--line); }

  .welcome-title { left: 59px; top: 878px; font-family: "Questrial", sans-serif; font-weight: 400; font-size: 24px; color: var(--navy); letter-spacing: 0.5px; }
  .welcome-text { left: 59px; top: 914px; width: 555px; font-size: 11.3px; line-height: 20.4px; }
  .btn { left: 59px; top: 1040px; width: 100px; height: 33px; background: var(--navy); color: #fff; font-size: 11.5px; font-weight: 700; text-align: center; line-height: 33px; }

  .news { left: 629px; top: 884px; width: 263px; height: 189px; border: 1px solid var(--line); }
  .news-title { position: absolute; left: 15px; top: 12px; font-family: "Questrial", sans-serif; font-weight: 400; font-size: 22px; color: var(--navy); }
  .news-item { position: absolute; left: 16px; width: 230px; font-size: 11.2px; line-height: 16px; }
  .news-date { margin-top: 7px; font-weight: 700; font-size: 11px; color: var(--navy); }
  .news-rule { position: absolute; left: 16px; width: 230px; top: 110px; height: 1px; background: var(--line); }

  .footer { left: 0; top: 1098px; width: 950px; height: 102px; background: linear-gradient(var(--footer-top), var(--footer-bottom)); }
  .footer-links { left: 59px; top: 1121px; font-family: "Questrial", sans-serif; font-size: 12.8px; color: var(--navy); word-spacing: 1px; }
  .footer-links .sep { color: var(--ink); margin: 0 8px; }
  .copyright { left: 59px; top: 1147px; font-size: 9px; line-height: 15.5px; color: var(--ink-dark); letter-spacing: 0.2px; }
  .follow { left: 775px; top: 1126px; font-size: 11px; font-weight: 700; color: var(--navy); }
  .social { left: 776px; top: 1149px; display: flex; gap: 9px; }
  .social span { width: 22px; height: 22px; border-radius: 3px; }
  .s1 { background: #3b5a98; } .s2 { background: #4fb1de; } .s3 { background: #1c6fa8; } .s4 { background: #ef7a1c; }
</style>
</head>
<body>
<div class="canvas">
  <div class="abs topbar"></div>

  <header>
    <div class="abs brand">Ironwood Signal Solutions</div>
    <div class="abs call">
      <div class="call-label">Call Us:</div>
      <div class="call-number">1-800-555-0142</div>
    </div>
  </header>

  <nav class="abs nav">
    <a style="left:59px">Home</a>
    <a style="left:134px">Phone Systems</a>
    <a style="left:269px">Carrier</a>
    <a style="left:350px">Video Surveillance</a>
    <a style="left:510px">Low Voltage Cabling</a>
    <a style="left:686px">Contact us</a>
  </nav>

  <section class="abs hero">
    <div class="hero-photo" role="img" aria-label="Photo of a black conference speakerphone on a wooden table"></div>
    <div class="abs hero-title">
      <div class="big">Ironwood Signal</div>
      <div class="small">Solutions</div>
    </div>
    <p class="abs hero-text">We provide PBX and IP/Cloud Based phone systems. We also sell and install video camera surveillance systems and provide low voltage cabling services.</p>
    <div class="abs dots"><span class="on"></span><span></span><span></span><span></span></div>
  </section>

  <section class="services">
    <div class="abs card" style="left:59px">
      <h3 class="card-title">PBX &amp; IP Phone Systems</h3>
      <p class="card-text">Vivamus egestas risus in magna varius commodo. Sed semper viverra egestas. Etiam pretium porttitor lectus, vel ornare neque porta volutpat.</p>
    </div>
    <div class="abs card-shadow" style="left:59px"></div>
    <div class="abs card-photo" style="left:109px;background:radial-gradient(circle at 50% 60%,#7a7f86,#3b3029 65%,#5a4535)" role="img" aria-label="Photo of an IP desk phone"></div>

    <div class="abs card" style="left:345px">
      <h3 class="card-title">Video Surveillance</h3>
      <p class="card-text">Vivamus egestas risus in magna varius commodo. Sed semper viverra egestas. Etiam pretium porttitor lectus, vel ornare neque porta volutpat.</p>
    </div>
    <div class="abs card-shadow" style="left:345px"></div>
    <div class="abs card-photo" style="left:395px;background:radial-gradient(circle at 50% 50%,#c3c7cc,#7ea7d8 45%,#5f93d2)" role="img" aria-label="Photo of security cameras against a blue sky"></div>

    <div class="abs card" style="left:630px">
      <h3 class="card-title">Low Voltage Cabling</h3>
      <p class="card-text">Vivamus egestas risus in magna varius commodo. Sed semper viverra egestas. Etiam pretium porttitor lectus, vel ornare neque porta volutpat.</p>
    </div>
    <div class="abs card-shadow" style="left:630px"></div>
    <div class="abs card-photo" style="left:680px;background:linear-gradient(135deg,#e8e8ea 10%,#e5352f 35%,#f3c21c 55%,#2a78d6 75%,#e9e9eb 95%)" role="img" aria-label="Photo of colored network cables with connectors"></div>
  </section>

  <div class="abs divider"></div>

  <section>
    <h2 class="abs welcome-title">Welcome to Our Website</h2>
    <p class="abs welcome-text">Aliquam molestie, mi et imperdiet euismod, dui purus auctor tellus, et interdum lacus lectus et ante. Sed accumsan sollicitudin sapien, sit amet adipiscing turpis gravida ac. In congue, neque ac lobortis volutpat, libero mauris varius mi, vitae suscipit ipsum ligula vitae risus. Duis aliquam nibh a dui iaculis viverra id a velit. Vivamus egestas risus in magna varius commodo. Sed semper viverra egestas. Etiam pretium porttitor lectus, vel ornare neque porta volutpat.</p>
    <a class="abs btn">Read More</a>
  </section>

  <aside class="abs news">
    <h2 class="news-title">News</h2>
    <div class="news-item" style="top:52px">
      <p>Sed semper viverra egestas. Etiam pretium porttitor lectus, vel ornare neque porta</p>
      <p class="news-date">Nov 5, 2015</p>
    </div>
    <div class="news-rule"></div>
    <div class="news-item" style="top:126px">
      <p>Sed semper viverra egestas. Etiam pretium porttitor lectus, vel ornare neque porta</p>
      <p class="news-date">Nov 5, 2015</p>
    </div>
  </aside>

  <footer>
    <div class="abs footer"></div>
    <div class="abs footer-links">Home<span class="sep">/</span>Phone systems<span class="sep">/</span>Carrier<span class="sep">/</span>Video Surveillance<span class="sep">/</span>Low Voltage Cabling<span class="sep">/</span>Contact Us</div>
    <div class="abs copyright">Copyright © 2015. Company Name All Right Reserved<br>Terms &amp; Services&nbsp; / &nbsp;Privacy Policy</div>
    <div class="abs follow">Follow Us</div>
    <div class="abs social"><span class="s1"></span><span class="s2"></span><span class="s3"></span><span class="s4"></span></div>
  </footer>
</div>
</body>
</html>
```